Linkmesa and Glimtoria advertising

We need Linkmesa and Glimtoria ads. Simple ad with Alaska themed background.
This ad is to introduce our new ZENIRO Internet service.
--Speeds to 500 mpbs
-- Packages start at only $89.99 for speeds to 100mbps
-- Fiber Optic based connection, Not satellite
-- Extreme low latency, consistent speeds
--FREE equipment, FREE Installation, FREE wifi router, First month of service FREE

```html
<!DOCTYPE html>
<html lang="en">
<head>
<meta charset="UTF-8">
<title>ZENIRO Internet Service Ad</title>
<link rel="stylesheet" href="https://fonts.googleapis.com/css2?family=Montserrat:wght@400;500;700;800&family=Poppins:wght@600;700&family=Inter:wght@500;600&display=swap">
<style>
  :root {
    --navy-deep: #0b2a5c;
    --navy: #14386f;
    --forest: #1d3a36;
    --white: #ffffff;
    --red: #e02227;
    --brand-ink: #1c1c1c;
  }
  * { margin: 0; padding: 0; box-sizing: border-box; }
  html, body { width: 1200px; height: 1200px; overflow: hidden; }
  body { font-family: "Montserrat", sans-serif; color: var(--white); }

  .ad { position: relative; width: 1200px; height: 1200px; overflow: hidden; }
  .ad-background {
    position: absolute; inset: 0;
    background: linear-gradient(180deg,
      #5b7694 0%, #8ea6bd 10%, #3f5c7a 24%,
      var(--forest) 42%, #263f3a 56%,
      #20506f 68%, var(--navy) 80%, var(--navy-deep) 100%);
  }

  .brand-box {
    position: absolute; left: 750px; top: 0;
    width: 381px; height: 155px;
    background: var(--white);
    border-radius: 0 0 26px 26px;
    display: flex; align-items: center; justify-content: center;
  }
  .brand-name {
    font-family: "Inter", sans-serif; font-weight: 600; font-size: 36px;
    color: var(--brand-ink);
  }

  .headline-block { position: absolute; left: 40px; width: 680px; text-align: center; }
  .service-name { top: 110px; font-weight: 700; line-height: 1; }
  .service-name .initial { font-size: 118px; letter-spacing: -2px; }
  .service-name .rest { font-size: 62px; letter-spacing: 1px; }
  .service-sub {
    top: 228px;
    font-family: "Poppins", sans-serif; font-weight: 700; font-size: 27px;
  }
  .speed-line { top: 298px; font-size: 44px; font-weight: 500; letter-spacing: 1px; }
  .speed-line strong { font-size: 60px; font-weight: 700; }

  .price-tag {
    position: absolute; left: 149px; top: 372px;
    width: 461px; height: 46px;
    background: var(--red);
    font-weight: 700; font-size: 27px;
    display: flex; align-items: center; justify-content: center;
  }
  .price {
    top: 432px;
    font-family: "Poppins", sans-serif; font-weight: 700; font-size: 86px; line-height: 1;
  }
  .price-note { top: 533px; font-size: 35px; font-weight: 500; letter-spacing: 0.5px; }

  .router-area {
    position: absolute; left: 694px; top: 189px;
    width: 452px; height: 428px;
    border-radius: 40px;
    background: radial-gradient(ellipse at 55% 70%,
      rgba(236,240,244,0.30) 0%, rgba(236,240,244,0.12) 45%, rgba(236,240,244,0) 75%);
  }

  .connection {
    position: absolute; left: 0; top: 656px; width: 1200px; text-align: center;
    font-family: "Poppins", sans-serif; font-weight: 700;
  }
  .connection .lead { font-size: 50px; letter-spacing: 0.5px; line-height: 1.2; }
  .connection .rule { width: 894px; height: 2px; background: var(--white); margin: 6px auto 2px; }
  .connection .emph { font-size: 76px; line-height: 1.1; }

  .benefit {
    position: absolute; left: 0; top: 826px; width: 1200px;
    font-family: "Inter", sans-serif; font-weight: 600; font-size: 39px;
    display: flex; align-items: center; justify-content: center; gap: 14px;
  }

  .free-badge { position: absolute; left: 190px; top: 868px; width: 310px; height: 300px; }
  .free-list {
    position: absolute; left: 508px; top: 926px;
    list-style: none;
    font-family: "Inter", sans-serif; font-weight: 500; font-size: 40px; line-height: 52px;
  }
  .free-list b { font-weight: 700; }
</style>
</head>
<body>
<div class="ad">
  <div class="ad-background" role="img" aria-label="Alaskan snowy mountain range above a dense evergreen forest, fading into a glowing blue network globe"></div>

  <div class="brand-box">
    <span class="brand-name">Northvale Satellite</span>
  </div>

  <div class="headline-block service-name"><span class="initial">Z</span><span class="rest">ENIRO</span></div>
  <div class="headline-block service-sub">INTERNET SERVICE</div>

  <div class="headline-block speed-line">SPEEDS TO <strong>500 MPBS</strong></div>
  <div class="price-tag">PACKAGES START AT ONLY</div>
  <div class="headline-block price">$89.99</div>
  <div class="headline-block price-note">FOR SPEEDS TO 100MBPS</div>

  <div class="router-area" role="img" aria-label="Photo of a white wifi router with two antennas"></div>

  <div class="connection">
    <div class="lead">FIBER OPTIC BASED CONNECTION,</div>
    <div class="rule"></div>
    <div class="emph">NOT SATELLITE</div>
  </div>

  <div class="benefit">
    <svg width="36" height="30" viewBox="0 0 34 28" aria-hidden="true">
      <path d="M3 15 L12 24 L31 4" fill="none" stroke="#ffffff" stroke-width="5" stroke-linecap="round" stroke-linejoin="round"/>
    </svg>
    <span>Extreme Low Latency, Consistent Speeds</span>
  </div>

  <svg class="free-badge" viewBox="0 0 310 300" aria-label="Free">
    <circle cx="154" cy="149" r="122" fill="#e02227"/>
    <path d="M237 34 L256 10 L264 17 Z" fill="#e02227"/>
    <path d="M256 54 L290 46 L289 56 Z" fill="#e02227"/>
    <path d="M30 232 L6 236 L8 246 Z" fill="#e02227"/>
    <path d="M48 262 L24 286 L32 292 Z" fill="#e02227"/>
    <text x="154" y="176" text-anchor="middle" font-family="Poppins, sans-serif" font-weight="700" font-size="76" fill="#ffffff">FREE</text>
  </svg>

  <ul class="free-list">
    <li><b>FREE</b> equipment</li>
    <li><b>FREE</b> Installation</li>
    <li><b>FREE</b> wifi router</li>
    <li>First month of service <b>FREE</b></li>
  </ul>
</div>
</body>
</html>
```